Name card for fertilizer industry

We 1. produce liquid fertilizer 2. gardening supply 3. Import&Export gardening related product.
I want the name card double-sided(Chinese & English version)
detail has chinese charactor for name and address.
Updates
Target Market(s)
Farmers
Industry/Entity Type
Industry
Contact Information for Business Card
Name: Martin Lo (邱偉達)
TEL: +886-47-615204
FAX:+886-47-640173
MOBILE: +886-952-184-603
ADDRESS: No.58, Taoyuan Rd, Beiming Township, Lanping County , TAIWAN(R.O.C) 蘭平縣北明鎮桃源路58號
Look and feel
Each slider illustrates characteristics of the customer's brand and the style your logo design should communicate.

```html
<!DOCTYPE html>
<html lang="en">
<head>
<meta charset="utf-8">
<title>Verdantis Enterprise Co. – Name Card</title>
<link rel="stylesheet" href="https://fonts.googleapis.com/css2?family=Open+Sans:wght@300;400;700&family=Montserrat:wght@700&family=Noto+Sans+TC:wght@400;500&display=swap">
<style>
  :root{
    --bg:#d9d9d6;
    --card:#1b1b1b;
    --band:#454545;
    --band-edge:#2a2a2a;
    --green:#8cc63f;
    --teal:#3cb7c4;
    --grey-text:#8e8a86;
    --light-text:#c9c9c9;
    --white:#f2f2f2;
    --rule:#5a5a5a;
  }
  *{margin:0;padding:0;box-sizing:border-box}
  html,body{width:1200px;height:1000px;overflow:hidden}
  body{
    background:var(--bg);
    display:flex;align-items:center;justify-content:center;gap:48px;
    font-family:"Open Sans",Arial,sans-serif;
  }
  .card{
    position:relative;width:540px;height:316px;background:var(--card);
    overflow:hidden;box-shadow:0 6px 18px rgba(0,0,0,.18);
  }
  /* front */
  .card-front{display:flex;flex-direction:column;align-items:center;padding-top:52px}
  .brand-dot{width:86px;height:86px;border-radius:50%;background:var(--green)}
  .company-name{
    margin-top:22px;color:var(--grey-text);font-weight:300;font-size:21px;
    letter-spacing:1.5px;text-transform:uppercase;
  }
  .services{margin-top:16px;list-style:none;text-align:center}
  .services li{
    color:var(--light-text);font-weight:300;font-size:11.5px;letter-spacing:.8px;
    text-transform:uppercase;line-height:19px;
  }
  /* back */
  .back-band{position:absolute;inset:0}
  .corner-dot{position:absolute;top:16px;right:22px;width:44px;height:44px;border-radius:50%;background:var(--band-edge)}
  .person{position:absolute;top:98px;right:30px;text-align:right}
  .person-name{font-family:"Montserrat",Arial,sans-serif;font-weight:700;font-size:25px;color:var(--green)}
  .person-name .zh{font-family:"Noto Sans TC",sans-serif;font-weight:400;font-size:23px;margin-left:6px}
  .contacts{list-style:none;margin-top:14px}
  .contacts li{
    display:flex;justify-content:flex-end;align-items:center;gap:7px;
    color:var(--teal);font-size:12px;line-height:18px;
  }
  .contacts svg{width:11px;height:11px;fill:var(--teal)}
  .rule{position:absolute;left:30px;right:30px;top:236px;height:1px;background:var(--rule)}
  .address{position:absolute;left:30px;top:248px;color:var(--white)}
  .address .en{font-weight:700;font-size:12.5px;line-height:19px}
  .address .zh-line{font-size:11.5px;line-height:19px;color:var(--light-text)}
  .address .zh-line span{font-family:"Noto Sans TC",sans-serif;margin-left:4px}
</style>
</head>
<body>
  <section class="card card-front" aria-label="Card front">
    <div class="brand-dot"></div>
    <h1 class="company-name">Verdantis Enterprise Co.</h1>
    <ul class="services">
      <li>Produce liquid fertilizer</li>
      <li>Gardening supply</li>
      <li>Import&amp;Export gardening related product.</li>
    </ul>
  </section>

  <section class="card card-back" aria-label="Card back">
    <svg class="back-band" viewBox="0 0 540 316" preserveAspectRatio="none" aria-hidden="true">
      <path d="M200 0 H540 V150 C470 70 360 22 200 0 Z" fill="var(--band)"/>
      <path d="M200 0 C360 22 470 70 540 150 V162 C470 84 360 34 200 0 Z" fill="var(--band-edge)"/>
    </svg>
    <div class="corner-dot"></div>
    <div class="person">
      <h2 class="person-name">Martin Lo<span class="zh">(邱偉達)</span></h2>
      <ul class="contacts">
        <li><svg viewBox="0 0 12 12"><path d="M2.5 0.5l2 2.2-1 1.3a7 7 0 0 0 4.5 4.5l1.3-1 2.2 2-1.3 1.9C5 11 1 7 0.6 1.8z"/></svg>+886-47-615204</li>
        <li><svg viewBox="0 0 12 12"><path d="M2 0h8v3H2zM0 4h12v6H9V8H3v2H0zM3 9h6v3H3z"/></svg>+886-47-640173</li>
        <li><svg viewBox="0 0 12 12"><path d="M3 0h6a1 1 0 0 1 1 1v10a1 1 0 0 1-1 1H3a1 1 0 0 1-1-1V1a1 1 0 0 1 1-1zm0 1.5v8h6v-8z"/></svg>+886-952-184-603</li>
        <li><svg viewBox="0 0 12 12"><path d="M0 2h12v8H0zm1 1v.4l5 3.4 5-3.4V3z"/></svg>martin.lo@fernmail.com</li>
      </ul>
    </div>
    <div class="rule"></div>
    <address class="address" style="font-style:normal">
      <p class="en">No.58, Taoyuan Rd, Beiming Township, Lanping County</p>
      <p class="zh-line">TAIWAN(R.O.C)<span>蘭平縣北明鎮桃源路58號</span></p>
    </address>
  </section>
</body>
</html>
```